Business Card Design Project

Corvexa logo will be provided after
Front

Bram Oskarsen- Construction Manager

Ph: (61) 07 53182907
boskarsen@corvexa.com.au
PO Box 83 Kelbarra 4529

Back
Corvexa
EPCM

Oil - Gas - Mining

Industry/Entity Type

Business

Font styles to use
Sans Serif

Colors
faa54b

Requirements
Must have
• White Back Ground

```html
<!DOCTYPE html>
<html lang="en">
<head>
<meta charset="utf-8">
<title>Corvexa Business Card</title>
<link rel="stylesheet" href="https://fonts.googleapis.com/css2?family=Archivo+Black&family=Arimo:wght@400;700&display=swap">
<style>
  :root {
    --orange: #faa54b;
    --ink: #1c1c1c;
    --card: #ffffff;
    --backdrop: #e9e9ec;
    --edge: #d4d4d8;
  }
  * { margin: 0; padding: 0; box-sizing: border-box; }
  html, body { width: 1200px; height: 1000px; overflow: hidden; }
  body {
    background: var(--backdrop);
    position: relative;
    font-family: "Arimo", Arial, sans-serif;
    color: var(--ink);
  }
  .card {
    position: absolute;
    width: 560px;
    height: 320px;
    background: var(--card);
    border: 1px solid var(--edge);
    box-shadow: 0 10px 28px rgba(0,0,0,0.12);
  }
  /* Back side: brand */
  .card-back { left: 70px; top: 560px; }
  .brand {
    position: absolute;
    left: 70px;
    top: 108px;
    display: flex;
    align-items: center;
    gap: 16px;
  }
  .brand-name {
    font-family: "Archivo Black", "Arial Black", sans-serif;
    font-size: 62px;
    letter-spacing: 1px;
    color: var(--ink);
    line-height: 1;
  }
  .brand-dot {
    width: 34px; height: 34px;
    border-radius: 50%;
    background: var(--orange);
  }
  .brand-tagline {
    position: absolute;
    left: 74px;
    top: 184px;
    font-size: 19px;
    letter-spacing: 0.5px;
    color: var(--ink);
  }
  /* Front side: contact */
  .card-front { left: 570px; top: 80px; }
  .person-name {
    position: absolute;
    left: 40px;
    top: 34px;
    font-family: "Archivo Black", "Arial Black", sans-serif;
    font-size: 46px;
    color: var(--orange);
    letter-spacing: 1px;
    line-height: 1;
    white-space: nowrap;
  }
  .role-band {
    position: absolute;
    left: 30px;
    right: 30px;
    top: 86px;
    height: 38px;
    background: var(--orange);
    color: var(--card);
    font-family: "Arimo", Arial, sans-serif;
    font-weight: 700;
    font-size: 25px;
    line-height: 38px;
    padding-left: 64px;
  }
  .contact-list {
    position: absolute;
    left: 58px;
    top: 150px;
    list-style: none;
  }
  .contact-item {
    display: flex;
    align-items: center;
    gap: 16px;
    height: 44px;
    font-size: 21px;
    color: var(--ink);
  }
  .contact-icon { width: 22px; height: 22px; flex: none; }
</style>
</head>
<body>

  <section class="card card-front" aria-label="Business card front">
    <h1 class="person-name">BRAM OSKARSEN</h1>
    <div class="role-band">Construction Manager</div>
    <ul class="contact-list">
      <li class="contact-item">
        <svg class="contact-icon" viewBox="0 0 22 22" aria-hidden="true">
          <rect x="6" y="1.5" width="10" height="19" rx="1.5" fill="none" stroke="var(--orange)" stroke-width="1.8"/>
          <line x1="9" y1="17" x2="13" y2="17" stroke="var(--orange)" stroke-width="1.6"/>
        </svg>
        <span>(61) 07 53182907</span>
      </li>
      <li class="contact-item">
        <svg class="contact-icon" viewBox="0 0 22 22" aria-hidden="true">
          <rect x="1" y="4" width="20" height="14" fill="var(--orange)"/>
          <polyline points="1,4 11,12 21,4" fill="none" stroke="#ffffff" stroke-width="1.6"/>
        </svg>
        <span>boskarsen@corvexa.com.au</span>
      </li>
      <li class="contact-item">
        <svg class="contact-icon" viewBox="0 0 22 22" aria-hidden="true">
          <polygon points="11,3 2,11 5,11 5,19 17,19 17,11 20,11" fill="var(--orange)"/>
        </svg>
        <span>PO Box 83 Kelbarra 4529</span>
      </li>
    </ul>
  </section>

  <section class="card card-back" aria-label="Business card back">
    <div class="brand">
      <span class="brand-name">CORVEXA</span>
      <span class="brand-dot"></span>
    </div>
    <p class="brand-tagline">EPCM • Oil • Gas • Mining</p>
  </section>

</body>
</html>
```